Aviation security consulting company needs a website

We need a website design for Brell Ostavik, and aviation security consulting company. Brell Ostavik (www.brellostavik.example) is an aviation security consulting company that works with government and industry stakeholders in over 60 countries on aviation security strategy, governance, and oversight at the regulatory and operational level.
Brell Ostavik is strongly internationally focused.
The website required should be simple, corporate, serious, and communicate professionalism, reliability and honesty. We are trying to give the company a feeling of being well established.
The attached files include the company logo, along with examples of company web page styles that we like.
The Brell Ostavik website need only be around five pages long (landing page, who we are, our services, our clients, contact), though don't feel limited to only five pages.
The existing website (www.brellostavik.example) was rushed and put together using Wix. We don't love the existing website as it looks too amateur, so don't use it as a template.
There is no requirement for any online sales tools to be included in the site. The site is purely informational, with the option of people making contact via email.

```html
<!DOCTYPE html>
<html lang="en">
<head>
<meta charset="utf-8">
<title>Brell Ostavik – Aviation Security Consulting</title>
<link rel="stylesheet" href="https://fonts.googleapis.com/css2?family=Montserrat:wght@400;600;700&family=Open+Sans:wght@400;600&display=swap">
<style>
:root{
  --navy:#1b2a5e;
  --navy-dark:#0f1a45;
  --navy-deep:#111c4a;
  --ink:#333333;
  --muted:#555555;
  --grey-bg:#f1f1f1;
  --field:#e6e6e6;
  --rule:#cfcfcf;
  --white:#ffffff;
  --black:#1a1a1a;
}
*{box-sizing:border-box;margin:0;padding:0}
html,body{width:1200px;height:3267px;overflow:hidden}
body{background:var(--white);font-family:"Open Sans",Arial,sans-serif;color:var(--ink);position:relative}
.section{position:absolute;left:0;width:1200px}
.abs{position:absolute}

/* header */
.top-rule{position:absolute;left:15px;top:15px;width:1170px;height:4px;background:var(--navy)}
.brand{position:absolute;left:44px;top:56px;display:flex;align-items:center;gap:14px}
.brand-square{width:60px;height:60px;background:var(--navy)}
.brand-name{font-family:"Montserrat",Arial,sans-serif;font-weight:600;font-size:36px;color:var(--navy);letter-spacing:-0.5px}
.search{position:absolute;left:893px;top:74px;width:261px;height:35px;border:2px solid var(--navy);border-radius:4px;display:flex;align-items:center;padding:0 12px;font-size:15px;color:var(--ink)}
.search svg{position:absolute;right:10px;top:7px}

/* nav */
.main-nav{position:absolute;left:15px;top:146px;width:1170px;height:50px;background:var(--navy-deep);display:flex;align-items:center}
.nav-item{position:absolute;top:0;height:50px;line-height:50px;font-family:"Montserrat",Arial,sans-serif;font-weight:700;font-size:15px;color:var(--white);text-transform:uppercase}
.nav-item.is-active{background:#24377a;color:#6f8be0;padding:0 20px}

/* hero */
.hero{position:absolute;left:15px;top:196px;width:1170px;height:599px;background:linear-gradient(180deg,#2a3a72 0%,#5e7bab 35%,#8ea6c9 55%,#3a4f86 80%,#1b2a5e 100%)}
.hero-caption{position:absolute;left:0;top:650px;width:1200px;text-align:center;font-family:"Montserrat",Arial,sans-serif;font-size:27px;line-height:38px;color:var(--white)}
.hero-dots{position:absolute;top:770px;left:532px;display:flex;gap:8px}
.hero-dots span{width:30px;height:4px;background:rgba(255,255,255,.6)}
.hero-dots span:first-child{background:var(--navy)}

/* section headings */
.section-title{position:absolute;left:0;width:1200px;text-align:center;font-family:"Montserrat",Arial,sans-serif;font-weight:700;font-size:28px;color:var(--navy);text-transform:uppercase}
.divider{position:absolute;left:250px;width:702px;height:24px}
.divider::before,.divider::after{content:"";position:absolute;top:11px;width:320px;height:1px;background:var(--rule)}
.divider::before{left:0}.divider::after{right:0}
.divider i{position:absolute;left:339px;top:0;width:24px;height:24px;background:var(--navy)}
.divider.on-dark::before,.divider.on-dark::after{background:rgba(255,255,255,.4)}
.divider.on-dark i{background:var(--white)}
.body-copy{position:absolute;left:90px;width:1020px;text-align:center;font-size:13.5px;line-height:21px;color:var(--muted)}
.btn{position:absolute;height:39px;line-height:39px;text-align:center;font-family:"Montserrat",Arial,sans-serif;font-weight:700;font-size:15px;color:var(--white);background:var(--navy);border-radius:4px;text-transform:uppercase}

/* services */
.service-circle{position:absolute;width:110px;height:110px;border-radius:50%;background:var(--white);border:2px solid #bfc4d4;display:flex;align-items:center;justify-content:center}
.service-circle .disc{width:90px;height:90px;border-radius:50%;background:var(--navy);display:flex;align-items:center;justify-content:center}
.service-text{position:absolute;width:225px;font-size:13.5px;line-height:20px;color:var(--muted)}
.service-text h3{font-family:"Montserrat",Arial,sans-serif;font-weight:700;font-size:15px;color:var(--navy);line-height:22px}
.hub{position:absolute;left:527px;top:1394px;width:146px;height:148px;background:var(--navy)}

/* clients */
.clients-bg{position:absolute;left:15px;top:1782px;width:1170px;height:385px;background:linear-gradient(180deg,#2b3a70 0%,#1f2d62 55%,#3a4878 100%)}

/* testimonials */
.quote-box{position:absolute;left:226px;top:2324px;width:752px;height:153px;background:var(--white);border:1px solid #d6d6d6;border-radius:12px;padding:22px 60px 0 62px;font-size:14px;line-height:21px;color:var(--muted)}
.quote-box::after{content:"";position:absolute;left:30px;bottom:-14px;width:24px;height:24px;background:var(--white);border-right:1px solid #d6d6d6;border-bottom:1px solid #d6d6d6;transform:rotate(45deg)}
.quote-mark{position:absolute;font-family:Georgia,serif;font-weight:700;font-size:50px;color:var(--black);line-height:1}
.quote-author{position:absolute;left:228px;top:2498px;font-family:"Montserrat",Arial,sans-serif;font-style:normal;font-weight:600;font-size:17px;color:var(--black)}
.pager{position:absolute;left:568px;top:2547px;display:flex;gap:5px}
.pager span{width:13px;height:13px;border-radius:50%;border:1.5px solid #777}
.pager span:first-child{background:var(--black);border-color:var(--black)}

/* contact */
.field{position:absolute;background:var(--field);font-size:14px;color:var(--muted);padding:10px 16px}
.send{position:absolute;left:605px;top:2877px;width:105px;height:39px;background:var(--black);color:var(--white);font-family:"Montserrat",Arial,sans-serif;font-weight:700;font-size:14px;text-align:center;line-height:39px}

/* footer */
.footer{position:absolute;left:15px;top:2977px;width:1170px;height:242px;background:var(--navy-deep)}
.footer-brand{position:absolute;left:0;top:3012px;width:1200px;display:flex;justify-content:center;align-items:center;gap:14px}
.footer-brand .brand-square{width:54px;height:54px;background:none;border:3px solid var(--white)}
.footer-brand .brand-name{color:var(--white);font-size:34px}
.footer-rule{position:absolute;left:330px;top:3115px;width:540px;height:1px;background:rgba(255,255,255,.35)}
.footer-nav{position:absolute;left:330px;top:3120px;width:540px;display:flex;justify-content:space-between;font-family:"Montserrat",Arial,sans-serif;font-size:10px;letter-spacing:1.5px;color:var(--white);text-transform:uppercase}
.social{position:absolute;left:566px;top:3162px;display:flex;gap:4px}
.social span{width:20px;height:20px;border-radius:50%;border:2px solid var(--white)}
.copyright{position:absolute;left:15px;top:3219px;width:1170px;height:48px;background:#1c1c1c;color:#cfcfcf;font-size:12px;text-align:center;line-height:48px}
</style>
</head>
<body>

<header>
  <div class="top-rule"></div>
  <div class="brand"><span class="brand-square"></span><span class="brand-name">Brell Ostavik</span></div>
  <div class="search">Search Website
    <svg width="20" height="20" viewBox="0 0 20 20"><circle cx="8" cy="8" r="6" fill="none" stroke="#1b2a5e" stroke-width="2.5"/><line x1="12.5" y1="12.5" x2="18" y2="18" stroke="#1b2a5e" stroke-width="2.5"/></svg>
  </div>
</header>

<nav class="main-nav">
  <span class="nav-item is-active" style="left:198px">Home</span>
  <span class="nav-item" style="left:315px">Who We Are</span>
  <span class="nav-item" style="left:463px">What We Do</span>
  <span class="nav-item" style="left:610px">Clients</span>
  <span class="nav-item" style="left:718px">Testimonials</span>
  <span class="nav-item" style="left:873px">Contact</span>
</nav>

<section class="hero-block">
  <div class="hero" role="img" aria-label="Photo of a passenger jet flying through a cloudy blue sky beside a glass office tower"></div>
  <p class="hero-caption">Brell Ostavik works with government and industry on aviation security<br>regulatory and operational strategy, governance, and oversight.</p>
  <div class="hero-dots"><span></span><span></span><span></span><span></span></div>
</section>

<section class="section who" style="top:795px;height:375px;background:var(--grey-bg)"></section>
<h2 class="section-title" style="top:857px">Who We Are</h2>
<div class="divider" style="top:903px"><i></i></div>
<p class="body-copy" style="top:952px">Lorem ipsum dolor sit amet, consectetuer adipiscing elit, sed diam nonummy nibh euismod tincidunt ut laoreet dolore magna aliquam erat volutpat. Ut wisi enim ad minim veniam, quis nostrud exerci tation ullamcorper suscipit lobortis nisl ut aliquip ex ea commodo consequat. Duis autem vel eum iriure dolor in hendrerit in vulputate velit esse molestie consequat, vel illum dolore eu feugiat nulla facilisis at vero eros et accumsan et iusto odio dignissim qui blandit praesent luptatum zzril delenit augue duis dolore te feugait nulla facilisi.</p>
<span class="btn" style="left:455px;top:1072px;width:292px">More About Brell Ostavik</span>

<section class="section what" style="top:1170px;height:612px"></section>
<h2 class="section-title" style="top:1233px">What We Do</h2>
<div class="divider" style="top:1280px"><i></i></div>

<svg class="abs" style="left:0;top:1170px" width="1200" height="612" viewBox="0 0 1200 612">
  <g stroke="#b9bdc9" stroke-width="1.5" fill="none">
    <polyline points="419,211 460,247 527,247"/>
    <polyline points="781,211 740,247 673,247"/>
    <polyline points="419,381 460,320 527,320"/>
    <polyline points="781,381 740,320 673,320"/>
    <line x1="600" y1="372" x2="605" y2="437"/>
  </g>
</svg>
<div class="hub"></div>

<div class="service-circle" style="left:309px;top:1326px"><div class="disc">
  <svg width="50" height="46" viewBox="0 0 50 46" fill="#fff"><circle cx="25" cy="7" r="5"/><rect x="19" y="13" width="12" height="8" rx="3"/><rect x="24" y="21" width="2" height="6"/><rect x="8" y="26" width="34" height="2"/><rect x="8" y="26" width="2" height="6"/><rect x="40" y="26" width="2" height="6"/><rect x="24" y="26" width="2" height="6"/><circle cx="9" cy="35" r="4"/><circle cx="25" cy="35" r="4"/><circle cx="41" cy="35" r="4"/><rect x="4" y="40" width="10" height="6" rx="2"/><rect x="20" y="40" width="10" height="6" rx="2"/><rect x="36" y="40" width="10" height="6" rx="2"/></svg>
</div></div>
<div class="service-circle" style="left:781px;top:1326px"><div class="disc">
  <svg width="44" height="48" viewBox="0 0 44 48" fill="none" stroke="#fff" stroke-width="3"><path d="M8 10 h28 l-5 10 h-18 z"/><line x1="22" y1="2" x2="22" y2="10"/><line x1="17" y1="20" x2="15" y2="46"/><line x1="27" y1="20" x2="29" y2="46"/><line x1="10" y1="46" x2="34" y2="46"/></svg>
</div></div>
<div class="service-circle" style="left:309px;top:1496px"><div class="disc">
  <svg width="42" height="48" viewBox="0 0 42 48" fill="none" stroke="#fff" stroke-width="3"><path d="M21 3 L38 9 V24 C38 35 30 42 21 46 C12 42 4 35 4 24 V9 Z"/><path d="M21 10 L31 14 V24 C31 31 26 35 21 38 Z" fill="#fff" stroke="none"/></svg>
</div></div>
<div class="service-circle" style="left:781px;top:1496px"><div class="disc">
  <svg width="48" height="48" viewBox="0 0 48 48" fill="none" stroke="#fff" stroke-width="2.5"><circle cx="22" cy="24" r="18"/><ellipse cx="22" cy="24" rx="8" ry="18"/><line x1="4" y1="24" x2="40" y2="24"/><line x1="7" y1="15" x2="37" y2="15"/><line x1="7" y1="33" x2="37" y2="33"/><path d="M30 28 L46 20 L44 24 L34 30 Z" fill="#fff"/></svg>
</div></div>
<div class="service-circle" style="left:550px;top:1607px"><div class="disc">
  <svg width="52" height="24" viewBox="0 0 52 24" fill="#fff"><path d="M2 12 C2 10 6 9 10 9 L20 9 L14 1 L19 1 L30 9 L44 9 C49 9 50 11 50 12 C50 13 49 15 44 15 L30 15 L19 23 L14 23 L20 15 L10 15 C6 15 2 14 2 12 Z"/></svg>
</div></div>

<div class="service-text" style="left:76px;top:1327px"><h3>Regulators</h3>Strategic guidance, development of regulation, training, mentoring, and developing aviation security compliance tools.</div>
<div class="service-text" style="left:87px;top:1497px"><h3>Capacity Development</h3>Implementing economically sustainable solutions to aviation security challenges in the local environment.</div>
<div class="service-text" style="left:904px;top:1327px"><h3>Airports</h3>Ensuring security is incorporated into airport design, conducting security assessments and undertaking strategic planning.</div>
<div class="service-text" style="left:904px;top:1497px"><h3>Airlines</h3>Developing programs, conducting assessments, and provide strategic guidance, governance and change management.</div>
<div class="service-text" style="left:669px;top:1612px"><h3>Air Cargo</h3>Assisting air cargo operators meet aviation security obligations while ensuring facilitation and profitability are maintained.</div>

<section class="clients-block">
  <div class="clients-bg" role="img" aria-label="Photo of an airport apron with an aircraft and ground service vehicles, tinted navy"></div>
  <h2 class="section-title" style="top:1842px;color:var(--white)">Clients</h2>
  <div class="divider on-dark" style="top:1886px"><i></i></div>
  <p class="body-copy" style="top:1932px;color:var(--white)">Lorem ipsum dolor sit amet, consectetuer adipiscing elit, sed diam nonummy nibh euismod tincidunt ut laoreet dolore magna aliquam erat volutpat. Ut wisi enim ad minim veniam, quis nostrud exerci tation ullamcorper suscipit lobortis nisl ut aliquip ex ea commodo consequat. Duis autem vel eum iriure dolor in hendrerit in vulputate velit esse molestie consequat, vel illum dolore eu feugiat nulla facilisis at vero eros et accumsan et iusto odio dignissim qui blandit praesent luptatum zzril delenit augue duis dolore te feugait nulla facilisi.</p>
  <span class="btn" style="left:531px;top:2058px;width:140px;background:var(--navy-dark)">Learn More</span>
</section>

<section class="section testimonials" style="top:2167px;height:447px;background:var(--grey-bg)"></section>
<h2 class="section-title" style="top:2227px">Testimonials</h2>
<div class="divider" style="top:2273px"><i></i></div>
<blockquote class="quote-box">Lorem ipsum dolor sit amet, consectetuer adipiscing elit, sed diam nonummy nibh euismod tincidunt ut laoreet dolore magna aliquam erat volutpat. Ut wisi enim ad minim veniam, quis nostrud exerci tation ullamcorper suscipit lobortis nisl ut aliquip ex ea commodo consequat. Duis autem vel eum iriure dolor in hendrerit in vulputate velit esse molestie consequat, vel illum dolore eu feugiat nulla facilisis at vero.</blockquote>
<span class="quote-mark" style="left:243px;top:2336px">&#8220;</span>
<span class="quote-mark" style="left:398px;top:2420px">&#8221;</span>
<cite class="quote-author">Marisa Quell</cite>
<div class="pager"><span></span><span></span><span></span><span></span></div>

<section class="section contact" style="top:2614px;height:363px"></section>
<h2 class="section-title" style="top:2678px">Contact</h2>
<div class="divider" style="top:2724px"><i></i></div>
<div class="field" style="left:296px;top:2781px;width:299px;height:39px">Name</div>
<div class="field" style="left:296px;top:2829px;width:299px;height:39px">Email</div>
<div class="field" style="left:296px;top:2877px;width:299px;height:39px">Phone</div>
<div class="field" style="left:605px;top:2781px;width:301px;height:87px">Message</div>
<div class="send">SEND</div>

<footer>
  <div class="footer"></div>
  <div class="footer-brand"><span class="brand-square"></span><span class="brand-name">Brell Ostavik</span></div>
  <div class="footer-rule"></div>
  <div class="footer-nav"><span>Home</span><span>Who We Are</span><span>What We Do</span><span>Clients</span><span>Testimonials</span><span>Contact</span></div>
  <div class="social"><span></span><span></span><span></span></div>
  <div class="copyright">© 2016 BRELL OSTAVIK. ALL RIGHTS RESERVED.</div>
</footer>

</body>
</html>
```